Guaranteed Job - Sleek Sexy Business Card UV Spot

Im looking for a sleek and sexy business card, that resembles elite or VIP status status.
our business is corinvale.example
you can view our products on there, but our main audience for handing out our cards will be for people in the hospitality industry, so it will need to impress high management and CEO of hotels and restaurants, bars, clubs etc...
the card features will have UV spot on both sides, 400gsm stock. standard size.
Artwork should be 86 x 54mm + 2mm bleed = 90 x 58mm
it should have a nice "unique" uv spot pattern that highlights the card, not a repeated pattern, theres no originality there, and it will be disregarded.
The written material will be:
Corin Vale Hospitality College (logo)
Tobin Marsh
Director
Phone: 1300 615 737
Mobile: 0455 817 296
Email: info@corinvale.example
website: www.corinvale.example
I'm looking for originality here, i don't want just a simple stock card, want something that has a wow factor for people.
You will find the logo attached. you may invert the white to black words to suit the background as you please.
thank you and good luck
As a side note, ive received a lot of proposals, im too busy to give feedback to each and every one, so if i havent provided feedback for your design within 24 hours, then consider it not acceptable, and you could resubmit another design.
So far i have not seen any design that stood out for me, they all seem pretty generic. there nothing thats unique, i would figure for the amount that im offering, that people would put some more effort and creativity into the design.
so far over 200 designs submitted, and nothing i have seen looks very original, everything looks like a different variation of the same stuff, i said it very clearly i wanted something unique, the only thing that has come close to it so far is this one
Reason: Ive received alot of design concepts and i have reviewed everyone, but i havent had time to give feedback to every single one, only the ones that have interested me, if i havent responded, its because i havent found it good enough.
so far only a few design have been on par with what ive been looking for, an attractive eye popping design.
heres a few of them,
http://files.pixelbazaar.example/design_img/51736/62418/62418_2840915_51736_image.jpg
http://files.pixelbazaar.example/design_img/51736/68254/68254_2841377_51736_image.jpg
theyre, both unique and original, and eye catching, the only thing theyre missing is the sexyness.
if you still think you have some creativity left in your minds, then throw it on here.
Reason: Sorry guys for the delay, I was in a serious accident and out of commission for the past few months, I'm just slowly recovering now, please bare with me as i try to attend to this project, it may take me awhile as I have other projects that are on standby, I'm not 100% at the moment, so im extending the deadline for 2 weeks right now. Thanks for your patience.
Hospitality

```html
<!DOCTYPE html>
<html lang="en">
<head>
<meta charset="utf-8">
<title>Corin Vale Hospitality College — Business Card</title>
<link rel="stylesheet" href="https://fonts.googleapis.com/css2?family=Saira+Condensed:wght@500;600&display=swap">
<style>
  :root {
    --canvas: #e4e4e4;
    --card-blue: #5398d1;
    --card-white: #ffffff;
    --ink: #1c1c1c;
    --text-blue: #4a8fcb;
  }
  * { box-sizing: border-box; margin: 0; padding: 0; }
  html, body { width: 1200px; height: 1031px; overflow: hidden; }
  body {
    background: var(--canvas);
    font-family: "Saira Condensed", "Arial Narrow", sans-serif;
    position: relative;
  }
  .card {
    position: absolute;
    left: 300px;
    width: 600px;
    height: 386px;
    border-radius: 10px;
    overflow: hidden;
    background: var(--card-blue);
  }
  .card--front { top: 121px; }
  .card--back { top: 523px; }
  .card__pattern { position: absolute; inset: 0; width: 100%; height: 100%; }
  .card__pattern .band { fill: var(--card-white); }

  .brand {
    position: absolute;
    left: 178px;
    top: 112px;
    display: flex;
    align-items: center;
    gap: 14px;
  }
  .brand__square {
    width: 30px;
    height: 30px;
    background: var(--card-blue);
    flex: none;
  }
  .brand__name {
    font-weight: 600;
    color: var(--ink);
    font-size: 40px;
    line-height: 0.95;
    letter-spacing: 0.5px;
    text-transform: uppercase;
  }

  .holder {
    position: absolute;
    left: 48px;
    top: 176px;
    color: var(--text-blue);
    font-weight: 500;
  }
  .holder__name { font-size: 18px; letter-spacing: 0.6px; line-height: 1.1; }
  .holder__role { font-size: 14px; letter-spacing: 0.4px; line-height: 1.1; }

  .contacts {
    position: absolute;
    left: 338px;
    top: 150px;
    list-style: none;
    color: var(--text-blue);
    font-weight: 500;
    font-size: 17px;
    letter-spacing: 0.6px;
  }
  .contacts li { display: flex; align-items: center; gap: 8px; height: 22.5px; }
  .contacts svg { width: 14px; height: 14px; fill: var(--text-blue); flex: none; }
</style>
</head>
<body>

<section class="card card--front" aria-label="Card front">
  <svg class="card__pattern" viewBox="0 0 600 386" preserveAspectRatio="none" aria-hidden="true">
    <polygon class="band" points="0,60 600,60 600,290 0,290"/>
    <polygon class="band" points="92,0 200,0 140,386 32,386"/>
    <polygon class="band" points="212,0 222,0 164,386 154,386"/>
    <polygon class="band" points="60,0 68,0 10,386 2,386"/>
    <polygon class="band" points="560,0 566,0 520,386 514,386"/>
    <polygon class="band" points="578,0 584,0 540,386 534,386"/>
  </svg>
  <div class="brand">
    <span class="brand__square"></span>
    <p class="brand__name">Corin Vale<br>Hospitality College</p>
  </div>
</section>

<section class="card card--back" aria-label="Card back">
  <svg class="card__pattern" viewBox="0 0 600 386" preserveAspectRatio="none" aria-hidden="true">
    <polygon class="band" points="0,142 600,142 600,246 0,246"/>
    <polygon class="band" points="330,0 430,0 372,386 272,386"/>
    <polygon class="band" points="440,0 448,0 392,386 384,386"/>
    <polygon class="band" points="560,0 568,0 512,386 504,386"/>
    <polygon class="band" points="580,0 588,0 534,386 526,386"/>
    <polygon class="band" points="300,0 306,0 248,386 242,386"/>
  </svg>
  <div class="holder">
    <p class="holder__name">Tobin Marsh</p>
    <p class="holder__role">Director</p>
  </div>
  <ul class="contacts">
    <li>
      <svg viewBox="0 0 16 16" aria-hidden="true"><path d="M1 5c0-2 3-3 7-3s7 1 7 3v1h-4V5H5v1H1z M3 8h10l1 6H2z"/></svg>
      1300 615 737
    </li>
    <li>
      <svg viewBox="0 0 16 16" aria-hidden="true"><path d="M5 1h6a1 1 0 0 1 1 1v12a1 1 0 0 1-1 1H5a1 1 0 0 1-1-1V2a1 1 0 0 1 1-1zm0 2v9h6V3z"/></svg>
      0455 817 296
    </li>
    <li>
      <svg viewBox="0 0 16 16" aria-hidden="true"><path d="M1 3h14v10H1z M2 4l6 5 6-5" stroke="#fff" stroke-width="1"/></svg>
      info@corinvale.example
    </li>
    <li>
      <svg viewBox="0 0 16 16" aria-hidden="true"><circle cx="8" cy="8" r="7"/><path d="M1 8h14M8 1v14" stroke="#fff" stroke-width="1"/></svg>
      www.corinvale.example
    </li>
  </ul>
</section>

</body>
</html>
```